Etiketten-Design für Bier
Zielgruppe
Wie sind eine Brauerei und auch Limonadenhersteller. Zielgruppe sind alle Personen von 16-70.
Aufgabenstellung
In dieser Ausschreibung geht es um eine Etikettengarnitur (Hals- u. Bauchetikett) der Sorte PILS. Die komplette Serie mit Bieretiketten soll jedoch für alle 13 Biersorten neu erstellt werden. Der Gewinner erhält nach Verhandlung/Angebot ebenfalls alle weiteren Sorten. Wir könnten uns vorstellen, für alle Etikettenformate ein ähnliches Schema bzw. Grundgerüst zu verwenden. Sortenspezifisch wird dieses dann an die jeweilige Sorte angepasst. Es sollen nicht alle gleich aussehen und sich nur im Schriftzug unterscheiden. Es wäre zudem schön, wenn die sortentypischen Farben wieder in den neuen Etiketten aufgegriffen werden würden. Unsere Logo und der Slogan 'Leidenschaft Handwerk Qualität' sollte ebenfalls verwendet werden. Alle Stanzen (als Vektorgrafik), Formate, Beispiele, Texte sind im Upload zu finden. Aus Beispielen wie dem HELLES-Etikett können Logo usw. als Vektorgrafik entnommen werden.

```html
<!DOCTYPE html>
<html lang="de">
<head>
<meta charset="utf-8">
<title>Kellbach Pils – Etikettengarnitur</title>
<link rel="stylesheet" href="https://fonts.googleapis.com/css2?family=Inter:wght@400;500;600;800;900&family=Yellowtail&display=swap">
<style>
  :root {
    --hop-green: #b8d582;
    --hop-line: #cfe4a8;
    --ink: #111014;
    --paper: #ffffff;
  }
  * { margin: 0; padding: 0; box-sizing: border-box; }
  html, body { width: 923px; height: 1200px; overflow: hidden; background: var(--paper); }
  .canvas {
    position: relative; width: 923px; height: 1200px; background: var(--paper);
    font-family: "Inter", "Helvetica Neue", Arial, sans-serif; color: var(--ink);
  }

  /* Halsetikett */
  .neck-label { position: absolute; left: 60px; top: 68px; width: 335px; height: 230px; }
  .neck-label svg { position: absolute; inset: 0; }
  .neck-brand {
    position: absolute; left: 0; width: 100%; top: 86px; text-align: center;
    font-weight: 900; font-size: 36px; letter-spacing: -0.5px; color: var(--ink);
  }
  .neck-variety {
    position: absolute; left: 0; width: 100%; top: 139px; text-align: center;
    font-weight: 600; font-size: 18px; color: var(--paper);
  }
  .neck-origin {
    position: absolute; left: 0; width: 100%; top: 168px; text-align: center;
    font-size: 6px; color: var(--paper);
  }

  /* Bauchetikett */
  .body-label { position: absolute; left: 460px; top: 72px; width: 388px; height: 414px; background: var(--paper); }
  .body-top { position: absolute; left: 0; top: 0; width: 388px; height: 227px; background: var(--hop-green); overflow: hidden; }
  .hop-art { position: absolute; border-radius: 40% 50% 10% 10%; }
  .hop-art--cone { left: 0; top: 80px; width: 145px; height: 147px; background: radial-gradient(circle at 55% 40%, var(--hop-line), var(--hop-green) 70%); }
  .hop-art--leaves { left: 225px; top: 22px; width: 163px; height: 205px; background: radial-gradient(circle at 60% 55%, var(--hop-line), var(--hop-green) 72%); }
  .slogan {
    position: absolute; top: 26px; left: 38px; right: 30px;
    display: flex; justify-content: space-between;
    font-family: "Yellowtail", "Brush Script MT", "Segoe Script", cursive;
    font-size: 22px; line-height: 1; color: var(--ink);
  }
  .body-brand {
    position: absolute; left: 0; width: 100%; top: 262px; text-align: center;
    font-weight: 900; font-size: 58px; line-height: 1.1; letter-spacing: -1px; color: var(--ink);
  }
  .brewery-line {
    position: absolute; left: 0; width: 100%; top: 348px; text-align: center;
    font-weight: 500; font-size: 8.5px; letter-spacing: 0.1px;
  }
  .body-band {
    position: absolute; left: 0; bottom: 0; width: 388px; height: 40px; background: var(--hop-green);
    display: flex; align-items: center; justify-content: space-between; padding: 0 11px;
  }
  .band-abv { font-weight: 500; font-size: 14px; padding-top: 4px; }
  .band-variety { font-weight: 600; font-size: 28px; color: var(--paper); margin-left: 30px; }
  .band-volume { font-weight: 500; font-size: 14px; padding-top: 4px; }
  .band-volume .estimate { font-size: 20px; font-weight: 400; vertical-align: -2px; }
</style>
</head>
<body>
<main class="canvas">
  <section class="neck-label" aria-label="Halsetikett">
    <svg width="335" height="230" viewBox="0 0 335 230">
      <path d="M43 9 L104 37 A77 77 0 0 1 230 37 L290 9 L326 80 L166 223 L7 80 Z" fill="var(--hop-green)"/>
    </svg>
    <div class="neck-brand">Kellbach</div>
    <div class="neck-variety">PILS</div>
    <div class="neck-origin">Bier aus Lindenau - echt fränkisch</div>
  </section>

  <section class="body-label" aria-label="Bauchetikett">
    <div class="body-top">
      <div class="hop-art hop-art--cone" role="img" aria-label="Weiße Linienzeichnung einer Hopfendolde"></div>
      <div class="hop-art hop-art--leaves" role="img" aria-label="Weiße Linienzeichnung von Hopfenblättern"></div>
      <div class="slogan"><span>Handwerk</span><span>Qualität</span><span>Leidenschaft</span></div>
    </div>
    <div class="body-brand">Kellbach</div>
    <div class="brewery-line">PRIVATBRAUEREI SEIT 1937</div>
    <div class="body-band">
      <span class="band-abv">Alk. 4,8% vol</span>
      <span class="band-variety">PILS</span>
      <span class="band-volume"><span class="estimate">℮</span> 0,5 l</span>
    </div>
  </section>
</main>
</body>
</html>
```